Dentistry Office

We want a new design for a Dentist's office website.

The theme is: "We provide high quality, state-of-the-art, dental care in a comfortable, caring environment."

The site currently has a menu on the left of the page with about 40 items on it. There is a great deal of textual content on each page, plus several illustrations.

We want to do this using CSS, so we need specifications in the CSS for all possible elements. The CSS needs to be named in a logical manner for easy use.

Every dentist on the planet seems to use lots of Flash. We don't want to because it is so distracting. We are looking for an elegant solution targeting 24-55 age group, but not excluding anyone.

The following (from another dentist's site) can give you a taste of what we want to communicate on the site:

"After 20 years of teaching dentists how to refine their technique and many years of writing textbooks, I currently devote my time to my office and the hands-on practice of dentistry. I'd like to welcome you personally to my dental practice, and I invite you to meet my highly experienced team of professionals.

"We have offered complete dental care of the highest quality since 1978. We provide Preventive Services, Tooth Whitening and Cosmetic Dentistry for a beautiful smile, Endodontics (root canal treatment) to treat painful teeth, Sedation Dentistry so you can relax, and Dental Implants to restore what is missing. We offer total care.

"Our approach to your health is simple: We use our education, experience and dedication to provide every patient with superior dental care.

"This passion for excellence is not just a goal, but a standard every member of our team holds.

"We also pride ourselves with our state of the art procedures, training and technology. This includes creating a beautiful smile using techniques that preserve as much of the original tooth as possible.

"Our abilities are renowned throughout the dental profession and I hope if you have any questions you will contact us by an e-mail note, by phone or just by dropping by."

Keep in mind the screen shape and dimensions. Your design needs to work in the normal screen proportions, regardless of how it looks when you post it here. Scrolling is OK, but the first impression needs to work.

Keep in mind that there will be about 250 words, or more, on each page.

Competitors web sites:

http://www.brellwickdentist.example/

http://www.brellwickdentalcare.example/

http://www.grinsbybrellwickdental.example/

http://www.dorvanfamilydentalcare.example/

http://www.brellwickdental.example/

http://www.quimbertdental.example/

We need to compete with these.

Target Market(s)

Generally adults seeking the most experienced and comfortable-to-be-with dentist.

Industry/Entity Type

Training

Requirements
Must have
• Must stand apart from other dentists.
• Must be elegant.
• Must have a horizontal menu structure across all columns, NOT a vertical that requires scrolling, no popout, pop down, etc. menus.
• We are looking for something special.
• Do not waste your time or ours putting up templates and things you have used before.
• Personally, I do not see how someone outside the US can understand the northern California dental market. But you are welcome to try.
Should not have
• Flash or graphics that move
• The look of a template
• Folksy fonts
• Looks like you used it 20 times before

```html
<!DOCTYPE html>
<html lang="en">
<head>
<meta charset="utf-8">
<title>Brellwick Dentist – Harold Venmore</title>
<link rel="stylesheet" href="https://fonts.googleapis.com/css2?family=Arimo:ital,wght@0,400;0,700;1,700&family=Source+Sans+3:wght@400&display=swap">
<style>
:root{
  --cyan:#1eaed6;
  --cyan-text:#2f9fd0;
  --ink:#111;
  --grey-text:#7d7d7d;
  --nav-black:#050505;
  --nav-blue:#3a9fd0;
  --band-blue:#3498cc;
  --band-blue-light:#66b9e0;
  --panel-grey:#f2f2f2;
  --rule:#c9c9c9;
  --icon:#c4c4c4;
  --page-bg-top:#9a9a9a;
  --page-bg-mid:#e6e6e6;
}
*{margin:0;padding:0;box-sizing:border-box}
html,body{width:1021px;height:1200px;overflow:hidden}
body{
  background:linear-gradient(90deg,var(--page-bg-top) 0%,var(--page-bg-mid) 20%,var(--page-bg-mid) 80%,var(--page-bg-top) 100%);
  font-family:"Arimo",Arial,sans-serif;color:var(--ink);
}
.page{position:absolute;left:0;top:0;width:1000px;height:1175px;transform:scale(1.021);transform-origin:0 0}
.abs{position:absolute}

/* navigation */
.main-nav{left:0;top:0;width:1000px;height:27px}
.main-nav svg{position:absolute;left:0;top:0}
.main-nav a{position:absolute;top:9px;color:#fff;font-weight:700;font-size:11px;text-decoration:none;letter-spacing:.1px}

/* header */
.masthead{left:44px;top:27px;width:909px;height:191px;background:linear-gradient(180deg,#f7f7f7,#ececec)}
.brand-name{left:25px;top:49px;font-family:"Source Sans 3",sans-serif;font-size:28px;color:var(--cyan);line-height:1;letter-spacing:.2px}
.brand-person{left:25px;top:81px;font-family:"Source Sans 3",sans-serif;font-size:28px;color:var(--grey-text);line-height:1}
.tagline{left:25px;top:140px;font-family:"Source Sans 3",sans-serif;font-size:13.5px;color:var(--grey-text);line-height:19px}
.hero-photo{left:516px;top:0;width:393px;height:191px;background:linear-gradient(90deg,#ebe7e3 0%,#d9c2ae 35%,#c8a590 60%,#e6d4c0 100%)}
.black-band{left:44px;top:218px;width:909px;height:27px;background:#000}

/* service tiles */
.services{left:44px;top:245px;width:909px;height:111px;background:var(--panel-grey);display:flex}
.service{position:relative;height:111px;border-right:1px solid #d4d4d4}
.service:last-child{border-right:none}
.service h3{position:absolute;left:25px;top:11px;font-family:"Arimo",Arial,sans-serif;font-weight:400;font-size:14px;color:var(--cyan);white-space:nowrap}
.service svg{position:absolute}

/* blue band */
.office-photo{left:44px;top:356px;width:181px;height:144px;background:linear-gradient(180deg,#5f7a5a 0%,#8a7262 45%,#6b665c 75%,#9a9c98 100%)}
.intro-band{left:225px;top:356px;width:728px;height:144px;background:linear-gradient(90deg,var(--band-blue) 0%,var(--band-blue-light) 35%,var(--band-blue) 70%,#2f8fc6 100%);color:#fff;font-size:12.2px;line-height:16px;padding:15px 6px 15px 14px}
.intro-band p{margin-bottom:16px}
.intro-band .address{font-weight:700;margin-bottom:15px}

/* content */
.content{left:44px;top:500px;width:728px;height:675px;background:#fff}
.sidebar{left:772px;top:500px;width:181px;height:675px;background:#fff;border-left:1px solid var(--rule)}
.section-title{font-family:"Arimo",Arial,sans-serif;font-weight:400;font-size:14px;color:var(--cyan-text)}
.provides-title{left:25px;top:19px}
.provides-list{left:24px;top:52px;list-style:none;font-size:11.4px;line-height:16px}
.provides-list li{padding-left:15px;position:relative}
.provides-list li::before{content:"*";position:absolute;left:0;top:1px;color:var(--cyan-text);font-weight:700;font-size:17px}
.divider{left:4px;top:213px;width:720px;border-top:1px dashed var(--cyan-text)}
.commit-title{left:25px;top:239px}
.commitment{left:26px;top:272px;width:655px;font-size:11.6px;line-height:16px}
.commitment p{margin-bottom:16px}
.commitment .creed{color:var(--cyan-text);font-style:italic;font-weight:700}

.offer{left:0;top:0;width:181px;height:214px;background:linear-gradient(180deg,#c9ebfa,#e7f6fd);padding:54px 6px 0 14px}
.offer h4{font-size:15.6px;line-height:20px;font-weight:700;color:var(--cyan-text)}
.offer small{display:block;margin-top:14px;font-size:9.6px;line-height:12px;color:#222;padding-left:9px;text-indent:-9px;width:152px}
.hours-title{left:14px;top:239px}
.hours{left:14px;top:272px;font-size:10.8px;line-height:16px}
.hours b{display:block}
.side-link{left:14px;font-family:"Arimo",Arial,sans-serif;font-size:14px;color:var(--cyan-text)}
.contact{left:13px;top:560px;font-size:12px;line-height:16px;color:var(--cyan-text)}
.contact strong{font-size:13.5px}
.contact p{margin-bottom:16px}
</style>
</head>
<body>
<div class="page">

  <nav class="main-nav abs">
    <svg width="1000" height="27" viewBox="0 0 1000 27" aria-hidden="true">
      <polygon points="44,0 940,0 953,27 44,27" fill="var(--nav-black)"/>
      <polygon points="44,0 130,0 145,27 44,27" fill="var(--nav-blue)"/>
      <g stroke="#555" stroke-width="2">
        <line x1="312" y1="0" x2="325" y2="27"/>
        <line x1="502" y1="0" x2="515" y2="27"/>
        <line x1="655" y1="0" x2="668" y2="27"/>
        <line x1="775" y1="0" x2="788" y2="27"/>
      </g>
    </svg>
    <a style="left:70px" href="#">HOME</a>
    <a style="left:158px" href="#">WHY WE ARE DIFFERENT</a>
    <a style="left:339px" href="#">TECHNOLOGIES WE OFFER</a>
    <a style="left:533px" href="#">MEET DR. VENMORE</a>
    <a style="left:685px" href="#">OUR STAFF</a>
    <a style="left:798px" href="#">CONTACT US / LINKS</a>
  </nav>

  <header class="masthead abs">
    <div class="brand-name abs">BRELLWICK DENTIST</div>
    <div class="brand-person abs">Harold Venmore</div>
    <p class="tagline abs">Providing Cosmetic Dentistry Excellence to Patients in Brellwick,<br>Corvell County and the Harlan Valley Area.</p>
    <div class="hero-photo abs" role="img" aria-label="Two smiling patients"></div>
  </header>
  <div class="black-band abs"></div>

  <section class="services abs">
    <div class="service" style="width:181px">
      <h3>EDUCATION</h3>
      <svg style="left:72px;top:34px" width="44" height="70" viewBox="0 0 44 70" aria-hidden="true">
        <path d="M6 6 C14 0 20 6 22 6 C24 6 30 0 38 6 C44 12 40 26 36 34 C33 44 33 66 29 66 C25 66 25 44 22 40 C19 44 19 66 15 66 C11 66 11 44 8 34 C4 26 0 12 6 6Z" fill="#f8f8f8" stroke="var(--icon)" stroke-width="2"/>
      </svg>
    </div>
    <div class="service" style="width:180px">
      <h3>PREVENTATIVE</h3>
      <svg style="left:20px;top:34px" width="136" height="66" viewBox="0 0 136 66" aria-hidden="true">
        <path d="M4 58 L104 24 L112 22 L116 30 L108 34 L8 64 Z" fill="#f8f8f8" stroke="var(--icon)" stroke-width="2" stroke-linejoin="round"/>
        <rect x="104" y="4" width="26" height="18" rx="3" transform="rotate(-18 117 13)" fill="#eee" stroke="var(--icon)" stroke-width="2"/>
      </svg>
    </div>
    <div class="service" style="width:182px">
      <h3>COSMETICS</h3>
      <svg style="left:66px;top:42px" width="52" height="52" viewBox="0 0 52 52" aria-hidden="true">
        <g stroke="var(--icon)" stroke-width="9" stroke-linecap="round">
          <line x1="26" y1="5" x2="26" y2="47"/>
          <line x1="8" y1="16" x2="44" y2="36"/>
          <line x1="8" y1="36" x2="44" y2="16"/>
        </g>
      </svg>
    </div>
    <div class="service" style="width:185px">
      <h3>RESTORATIONS</h3>
      <svg style="left:52px;top:42px" width="84" height="58" viewBox="0 0 84 58" aria-hidden="true">
        <rect x="2" y="2" width="80" height="54" fill="#f6f6f6" stroke="var(--icon)" stroke-width="3"/>
        <rect x="6" y="6" width="72" height="46" fill="none" stroke="var(--icon)" stroke-width="1.5"/>
        <path d="M35 12 H49 V22 H60 V36 H49 V46 H35 V36 H24 V22 H35 Z" fill="#ececec" stroke="var(--icon)" stroke-width="2"/>
      </svg>
    </div>
    <div class="service" style="width:181px">
      <h3 style="left:15px">VISITING OUR OFFICE</h3>
      <svg style="left:50px;top:40px" width="66" height="64" viewBox="0 0 66 64" aria-hidden="true">
        <path d="M4 30 L33 4 L62 30 M12 23 V60 H54 V23" fill="#f6f6f6" stroke="var(--icon)" stroke-width="2.5" stroke-linejoin="round"/>
        <rect x="22" y="30" width="12" height="12" fill="none" stroke="var(--icon)" stroke-width="2"/>
        <path d="M40 60 V40 H48 V60" fill="none" stroke="var(--icon)" stroke-width="2"/>
        <path d="M20 64 C30 54 44 56 54 48" fill="none" stroke="var(--icon)" stroke-width="2"/>
      </svg>
    </div>
  </section>

  <div class="office-photo abs" role="img" aria-label="Dental office building among trees"></div>
  <section class="intro-band abs">
    <p class="address">Located at 2240 Larkfield Avenue, Ste B-4, Brellwick, CA 95400</p>
    <p>In Brellwick, when you’re a patient of Dr. Venmore, you can be confident that you’re receiving care from the most experienced, knowledgeable, and skilled cosmetic dentist in Corvell County.</p>
    <p>Dr. Venmore is an award-winning leader in restorative dentistry and a genial professional. His humor, dedication, and talent ensure you a pleasant experience and superb, long-lasting results.</p>
  </section>

  <main class="content abs">
    <h2 class="section-title provides-title abs">DR. VENMORE PROVIDES</h2>
    <ul class="provides-list abs">
      <li><b>General dentistry</b> - oral hygiene, cavity detection and repair, crowns.</li>
      <li><b>Cosmetic/restorative dentistry</b> - broken or misshapen teeth, crooked smiles, unsightly gaps</li>
      <li><b>Non-metal fillings</b> - nontoxic, durable tooth-colored resin fillings that are proven to provide better results</li>
      <li><b>Tooth shaping</b> - extending, shortening or otherwise reshaping teeth for improved esthetics</li>
      <li><b>Complete smile make-over's</b> - resin veneers that reshape the whole mouth while preserving natural teeth</li>
      <li><b>Tooth whitening</b> - at-home bleaching options to make teeth appear years younger</li>
      <li><b>Laser Dentistry, Sleep Dentistry, and Implant Dentistry with the Finest and Latest Equipment and Materials.</b></li>
      <li><b>Dental Implants to replace missing teeth.</b></li>
      <li><b>Sedation Dentistry so you can be relaxed.</b></li>
    </ul>
    <div class="divider abs"></div>
    <h2 class="section-title commit-title abs">DR. VENMORE’ COMMITMENT</h2>
    <div class="commitment abs">
      <p>After 25 years of teaching dentists how to refine their technique and many years of writing textbooks, I currently devote my<br>time to my office and the hands-on practice of dentistry. I'd like to welcome you personally to my dental practice, and I invite<br>you to meet my highly experienced team of professionals.</p>
      <p>Dr. Venmore and his Associated have offered complete dental care of the highest quality since 1981. We provide Preventive<br>Services, Tooth Whitening and Cosmetic Dentistry for a beautiful smile, Endodontics (root canal treatment) to treat painful teeth,<br>Sedation Dentistry so you can relax, and Dental Implants to restore what is missing. We offer total care.</p>
      <p class="creed">Our approach to your health is simple: We use our education, experience and dedication to provide every patient with<br>superior dental care.</p>
      <p class="creed">This passion for excellence is not just a goal, but a standard every member of our team holds.</p>
      <p>We also pride ourselves with our state of the art procedures, training and technology. This includes creating a beautiful<br>smile using techniques that preserve as much of the original tooth as possible.</p>
      <p>Our abilities are renowned throughout the dental profession and I hope if you have any questions you will contact us by an<br>e-mail note, by phone or just by dropping by.</p>
      <p>Thank you.</p>
      <p>Sincerely,</p>
      <p>Harold Venmore, DDS FAGD</p>
    </div>
  </main>

  <aside class="sidebar abs">
    <div class="offer abs">
      <h4>We offer an Initial Patient Examination, X-rays and Cleaning for $84.00.</h4>
      <small>**New patients only. Offers are<br>cash patients only. Insurance<br>will be billed at full value.</small>
    </div>
    <h2 class="section-title hours-title abs">OFFICE HOURS</h2>
    <div class="hours abs">
      <b>Our usual office hours are:</b>
      Monday 8 am to 6 pm<br>
      Tuesday 8 am to 5 pm<br>
      Wednesday 8 am to 5 pm<br>
      Thursday 8 am to 5 pm<br>
      Friday 7:00 am to 4 pm
    </div>
    <a class="side-link abs" style="top:400px">MAP TO OFFICE</a>
    <a class="side-link abs" style="top:432px">WHERE TO STAY?</a>
    <div class="contact abs">
      <p>Please contact us at<br><strong>(555) 014-2290.</strong></p>
      <p>To contact us outside office hours for an emergency, please call <strong>(555) 018-4471.</strong></p>
    </div>
  </aside>

</div>
</body>
</html>
```